Gourmet food company looking for a dazzling label for their premuim vinagrette dressings

Need a food label that will dazzle our customer and prove what a premium product we have. We make high end gourmet dressing for vegetables, fruit, meat, poultry and fish.

Our label will fit on a 250 mil Tolvenna Square bottle. Labels should be a 4x5 or even 5x5 depending on the design. Nutritionals, bar codes and company blurb will be supplied later. We really want to test you all's talent on this one and are very excited to see your renderings!

Our dressings are Champagne Pear Vinaigrette, White Balsmic Vinaigrette, Mojito Lime Vinaigrette, Creamy-Avacado Lime Vinaigrette, and Asian Sesame Vinaigrette. I hope these names will help you envision our product and kinda what we are looking for.

Thank you all so far for your renderings.I really don't want pictures if that helps. Our logo can be smaller and/or the name of the product bigger. Perhaps we can even redesign Lumora and remove the leaf as I don't really care for what I see yet.So good luck and thanks Added Friday, August 19, 2016

I am still looking for that clean - elegant design for our product as our product is just that. If you look on the internet at vinegars and oils you will see many designs that are simple yet elegant. Creative lettering, bordering, color (can be black and white) and size will help accomplish this. So I invite you to use all your creativity and help me find just what we need.Many thanks Added Tuesday, August 23, 2016

Project Deadline Extended Reason: So many great designs coming in that I wanted a few extra days to tweek!Great job all Added Friday, August 26, 2016

Project Deadline Extended Reason: Very good designs thus far. We just need a few more days.Thanks Added Wednesday, August 31, 2016

Target Market(s)

High end grocery and specialty stores.

Our side panel on the label will say "At Lumora we're fanatics for great flavors and are passionate about finding the best ingredients. From simple to elegant our products are "simply lumora".

Industry/Entity Type

It Company

Font styles to use
Serif
Decorative
Script

Requirements
Must have
• A label that will draw the consumer to pick it up! Need something bold and elegant...
Nice to have
• Again, I really would like to have a label that pops. Since the bottle front is only about 2inches in width it will need some creativity. Would like something very simple and elegant.
• If the designer does not like the logo, please feel free to design without it!
Should not have
• Dark dark colors. We are selling dressing and we don't want any colors that may distort the contents.
• No stock photos for the front. I don't want our dressing to look like the others on the self. Brackwell Pantry just uses lettering and a their packaging is eye catching

```html
<!DOCTYPE html>
<html lang="en">
<head>
<meta charset="utf-8">
<title>Lumora Vinaigrette Labels</title>
<link rel="stylesheet" href="https://fonts.googleapis.com/css2?family=Jost:wght@300;600&family=Lobster&display=swap">
<style>
  :root {
    --canvas: #ffffff;
    --label-green: #0b6a3b;
    --label-shade: #095c33;
    --wedge-avocado: #053d0d;
    --wedge-sesame: #f7d531;
    --wedge-mojito: #2ec043;
    --ink-light: #ffffff;
    --series-number: #7dd3b1;
  }
  html, body {
    margin: 0;
    padding: 0;
    overflow: hidden;
    background: var(--canvas);
  }
  .canvas {
    position: relative;
    width: 1200px;
    height: 1013px;
    background: var(--canvas);
    overflow: hidden;
  }
  .series-number {
    position: absolute;
    left: 54px;
    top: 96px;
    margin: 0;
    font-family: "Jost", sans-serif;
    font-weight: 300;
    font-size: 40px;
    color: var(--series-number);
  }
  .label {
    position: absolute;
    top: 325px;
    width: 184px;
    height: 582px;
  }
  .label--avocado { left: 167px; }
  .label--sesame  { left: 507px; }
  .label--mojito  { left: 842px; }
  .label svg { display: block; width: 100%; height: 100%; }
  .label__base { fill: var(--label-green); }
  .label__shade { fill: var(--label-shade); }
  .wedge--avocado { fill: var(--wedge-avocado); }
  .wedge--sesame  { fill: var(--wedge-sesame); }
  .wedge--mojito  { fill: var(--wedge-mojito); }
  .brand-name {
    font-family: "Jost", sans-serif;
    font-weight: 600;
    font-size: 24px;
    letter-spacing: 3px;
    fill: var(--ink-light);
  }
  .flavour-name {
    font-family: "Lobster", cursive;
    font-size: 19px;
    fill: var(--ink-light);
  }
  .volume {
    font-family: "Lobster", cursive;
    font-size: 8px;
    fill: var(--ink-light);
  }
</style>
</head>
<body>
<main class="canvas">
  <p class="series-number">1.</p>

  <figure class="label label--avocado" style="margin:0">
    <svg viewBox="0 0 184 582" xmlns="http://www.w3.org/2000/svg">
      <defs>
        <clipPath id="shape-avocado"><path d="M0 582 V78 C0 30 40 0 92 0 C144 0 184 30 184 78 V582 Z"/></clipPath>
      </defs>
      <g clip-path="url(#shape-avocado)">
        <rect class="label__base" width="184" height="582"/>
        <rect class="label__shade" x="150" width="34" height="582"/>
        <polygon class="wedge--avocado" points="28,0 156,0 100,500 82,500"/>
      </g>
      <text class="brand-name" x="92" y="76" text-anchor="middle">LUMORA</text>
      <text class="flavour-name" x="92" y="520" text-anchor="middle">Creamy-Avacado</text>
      <text class="flavour-name" x="92" y="544" text-anchor="middle">Lime Vinaigrette</text>
      <text class="volume" x="92" y="560" text-anchor="middle">250ml</text>
    </svg>
  </figure>

  <figure class="label label--sesame" style="margin:0">
    <svg viewBox="0 0 184 582" xmlns="http://www.w3.org/2000/svg">
      <defs>
        <clipPath id="shape-sesame"><path d="M0 582 V78 C0 30 40 0 92 0 C144 0 184 30 184 78 V582 Z"/></clipPath>
      </defs>
      <g clip-path="url(#shape-sesame)">
        <rect class="label__base" width="184" height="582"/>
        <rect class="label__shade" x="150" width="34" height="582"/>
        <polygon class="wedge--sesame" points="28,0 156,0 100,500 82,500"/>
      </g>
      <text class="brand-name" x="92" y="74" text-anchor="middle">LUMORA</text>
      <text class="flavour-name" x="92" y="518" text-anchor="middle">Asian Sesame</text>
      <text class="flavour-name" x="92" y="542" text-anchor="middle">Vinaigrette</text>
      <text class="volume" x="92" y="558" text-anchor="middle">250ml</text>
    </svg>
  </figure>

  <figure class="label label--mojito" style="margin:0">
    <svg viewBox="0 0 184 582" xmlns="http://www.w3.org/2000/svg">
      <defs>
        <clipPath id="shape-mojito"><path d="M0 582 V78 C0 30 40 0 92 0 C144 0 184 30 184 78 V582 Z"/></clipPath>
      </defs>
      <g clip-path="url(#shape-mojito)">
        <rect class="label__base" width="184" height="582"/>
        <rect class="label__shade" x="150" width="34" height="582"/>
        <polygon class="wedge--mojito" points="28,0 156,0 100,500 82,500"/>
      </g>
      <text class="brand-name" x="92" y="76" text-anchor="middle">LUMORA</text>
      <text class="flavour-name" x="92" y="522" text-anchor="middle">Mojito Lime</text>
      <text class="flavour-name" x="92" y="546" text-anchor="middle">Vinaigrette</text>
      <text class="volume" x="92" y="562" text-anchor="middle">250ml</text>
    </svg>
  </figure>
</main>
</body>
</html>
```